Software Company Business Card Design

We are looking for a business card design for a software, messaging & IT services company based in Australia.

Talvora Group is the holding company for 3 brands all offering technology based business solutions; Talvora, Brindle & Quillpad. Brand Identity = Friendly, Professional, Viable, Vibrant, Creative

We want our business card to reflect that we are an innovative market leader. The design should be clean, professional and original.

This design will be used for all 3 brands.

More information about our company can be found at: www.talvoragroup.example.au
www.brindle.example.au

Details we would like on the card:

Firstname Lastname
Position
Level 17, 482 Ormond Rd
North Sydney
NSW 2060
Phone: +61 2 5550 1738
Fax: +61 2 5550 1794
Mobile:
Email:
www.talvoragroup.example.au

Target Market(s)

Our business cards are given to B2B and industry professionals.

Industry/Entity Type

Business

Requirements
Must have
• The Business Card must include the same colours as the logo.
Nice to have
• We would like it to me double sided.

```html
<!DOCTYPE html>
<html lang="en">
<head>
<meta charset="utf-8">
<title>Talvora Group — Business Card</title>
<link rel="stylesheet" href="https://fonts.googleapis.com/css2?family=PT+Sans:wght@400;700&display=swap">
<style>
  :root {
    --brand-magenta: #9b0047;
    --card-white: #ffffff;
    --mark-tint: #dcdced;
    --page-bg: #ffffff;
  }
  html, body {
    margin: 0;
    padding: 0;
    width: 1047px;
    height: 1200px;
    overflow: hidden;
    background: var(--page-bg);
  }
  .canvas {
    position: relative;
    width: 1047px;
    height: 1200px;
  }
  .card {
    position: absolute;
    width: 898px;
    height: 523px;
    filter: drop-shadow(2px 3px 4px rgba(0,0,0,0.35));
  }
  .card--front { left: 44px; top: 38px; }
  .card--back { left: 113px; top: 614px; }
  .card svg { display: block; width: 100%; height: 100%; }
  .fill-brand { fill: var(--brand-magenta); }
  .fill-white { fill: var(--card-white); }
  .fill-mark { fill: var(--mark-tint); opacity: 0.75; }
  .logo-box { fill: var(--card-white); stroke: var(--brand-magenta); stroke-width: 1; }
  .txt { font-family: "PT Sans", sans-serif; }
  .wordmark { font-size: 27px; font-weight: 700; fill: var(--brand-magenta); }
  .person-name { font-size: 14px; font-weight: 700; fill: var(--brand-magenta); }
  .person-role { font-size: 14px; fill: var(--brand-magenta); }
  .contact-light { font-size: 14px; fill: var(--card-white); }
  .contact-label { font-size: 13px; font-weight: 700; fill: var(--card-white); }
  .contact-number { font-size: 14px; fill: var(--brand-magenta); }
</style>
</head>
<body>
<main class="canvas">

  <!-- Front side -->
  <section class="card card--front" aria-label="Business card front">
    <svg viewBox="0 0 515 300" xmlns="http://www.w3.org/2000/svg">
      <rect class="fill-brand" x="0" y="0" width="515" height="300"/>
      <rect class="fill-white" x="12" y="8" width="493" height="282" rx="20"/>
      <path class="logo-box" d="M0.5 0.5 H218 V80 Q218 92 206 92 H0.5 Z"/>
      <circle class="fill-mark" cx="390" cy="175" r="100"/>
      <path class="fill-brand" d="M82 178 Q82 158 102 158 H515 V300 H82 Z"/>
      <circle class="fill-mark" cx="390" cy="175" r="100" opacity="0.18"/>
      <text class="txt wordmark" x="20" y="56">Talvora Group</text>

      <text class="txt person-name" x="346" y="118">Name Lastname</text>
      <text class="txt person-role" x="346" y="137">Position</text>

      <g class="contact-numbers">
        <rect class="fill-white" x="62" y="192" width="150" height="62"/>
        <rect class="fill-brand" x="62" y="193" width="19" height="18"/>
        <rect class="fill-brand" x="62" y="213" width="19" height="18"/>
        <rect class="fill-brand" x="62" y="233" width="19" height="20"/>
        <text class="txt contact-label" x="64" y="207">P:</text>
        <text class="txt contact-label" x="64" y="227">F:</text>
        <text class="txt contact-label" x="64" y="248">M</text>
        <text class="txt contact-number" x="86" y="207">+61 2 5550 1738</text>
        <text class="txt contact-number" x="86" y="227">+61 2 5550 1794</text>
        <text class="txt contact-number" x="86" y="248">0000 000 000</text>
      </g>

      <text class="txt contact-light" x="285" y="191">Level 17, 482 Ormond Rd,</text>
      <text class="txt contact-light" x="285" y="209">North Sydney,</text>
      <text class="txt contact-light" x="285" y="227">NSW 2060</text>
      <text class="txt contact-light" x="285" y="252">www.talvoragroup.example.au</text>
      <text class="txt contact-light" x="285" y="271">E: info@talvoragroup.example.au</text>
    </svg>
  </section>

  <!-- Back side -->
  <section class="card card--back" aria-label="Business card back">
    <svg viewBox="0 0 515 300" xmlns="http://www.w3.org/2000/svg">
      <rect class="fill-brand" x="0" y="0" width="515" height="300"/>
      <rect class="fill-white" x="12" y="8" width="493" height="282" rx="20"/>
      <path class="logo-box" d="M0.5 0.5 H218 V80 Q218 92 206 92 H0.5 Z"/>
      <circle class="fill-mark" cx="430" cy="150" r="100"/>
      <path class="fill-brand" d="M81 178 Q81 158 101 158 H515 V300 H81 Z"/>
      <circle class="fill-mark" cx="430" cy="150" r="100" opacity="0.18"/>
      <text class="txt wordmark" x="20" y="56">Talvora Group</text>

      <text class="txt contact-light" x="283" y="232">www.talvoragroup.example.au</text>
      <text class="txt contact-light" x="283" y="252">E: info@talvoragroup.example.au</text>
    </svg>
  </section>

</main>
</body>
</html>
```